Industrial Automation company requires a business card design

Valtrin Automation provides design & build of Automated Equipment for manufacturing industry.
www.valtrinautomation.example
The equipment we design is used for manufacturing in sectors such as medical device, pharmaceutical, aerospace and electronics.
We require a new business card design which incorporates our (New) logo and the key message words:
Automated Equipment:
Design, Build, Control, Test, Support

```html
<!DOCTYPE html>
<html lang="en">
<head>
<meta charset="utf-8">
<title>Valtrin Automation – Business Card</title>
<link rel="stylesheet" href="https://fonts.googleapis.com/css2?family=Lato:wght@400;700&display=swap">
<style>
  :root {
    --page-bg: #ffffff;
    --card-white: #f4f4f4;
    --brand-green: #047236;
    --brand-green-light: #0a7a3c;
    --brand-green-dark: #025f2c;
    --ink: #222222;
    --ink-soft: #333333;
    --rule: #3a3a3a;
  }
  * { margin: 0; padding: 0; box-sizing: border-box; }
  html, body {
    width: 1200px; height: 929px; overflow: hidden;
    background: var(--page-bg);
    font-family: "Lato", sans-serif;
  }
  .canvas { position: relative; width: 1200px; height: 929px; }

  .card {
    position: absolute; left: 341px; width: 518px;
    border-radius: 8px; overflow: hidden;
    box-shadow: 0 2px 4px rgba(0,0,0,0.35);
  }
  .card-front { top: 126px; height: 298px; background: var(--card-white); }
  .card-back {
    top: 457px; height: 295px;
    background: radial-gradient(ellipse at 50% 45%, var(--brand-green-light) 0%, var(--brand-green) 55%, var(--brand-green-dark) 100%);
  }

  .brand { position: absolute; display: flex; align-items: center; font-weight: 700; white-space: nowrap; }
  .brand-dot { border-radius: 50%; flex: none; }
  .card-front .brand { left: 26px; top: 132px; gap: 8px; color: var(--brand-green); font-size: 19px; }
  .card-front .brand-dot { width: 20px; height: 20px; background: var(--brand-green); }
  .card-back .brand { left: 0; right: 0; justify-content: center; top: 112px; gap: 12px; color: #ffffff; font-size: 34px; }
  .card-back .brand-dot { width: 34px; height: 34px; background: #ffffff; }

  .divider { position: absolute; left: 259px; top: 72px; width: 1px; height: 161px; background: var(--rule); }
  .divider::before { content: ""; position: absolute; left: 0; top: 0; width: 1px; height: 35px; background: var(--brand-green); }

  .person { position: absolute; left: 272px; top: 78px; }
  .person-name { font-size: 23px; font-weight: 700; color: var(--brand-green); line-height: 1.1; }
  .person-title { font-size: 14.5px; color: var(--ink); line-height: 1.2; }

  .contact { position: absolute; left: 271px; top: 143px; font-size: 14.5px; color: var(--ink-soft); line-height: 17.6px; }
  .contact-row { display: flex; align-items: center; gap: 6px; white-space: nowrap; }
  .contact-row svg { width: 15px; height: 13px; flex: none; fill: var(--brand-green); }
  .address { margin-bottom: 3px; }
  .web-accent { color: var(--brand-green); }

  .tagline-band {
    position: absolute; left: 0; right: 0; top: 260px; height: 21px;
    background: #ffffff; color: #111111; font-size: 14.5px;
    display: flex; align-items: center; justify-content: center;
  }
</style>
</head>
<body>
<div class="canvas">

  <section class="card card-front">
    <div class="brand"><span class="brand-dot"></span>Valtrin Automation</div>
    <div class="divider"></div>
    <div class="person">
      <div class="person-name">Dara Keane</div>
      <div class="person-title">President</div>
    </div>
    <div class="contact">
      <div class="address">Ardcullen, Rathmore<br>Co. Westmere, Ireland</div>
      <div class="contact-row">
        <svg viewBox="0 0 16 13" aria-hidden="true"><path d="M1 4c0-2 3-3 7-3s7 1 7 3v1h-4V3.5H5V5H1zM4 6h8l2 6H2z"/></svg>
        +353 (0) 21 555 0147
      </div>
      <div class="contact-row">
        <svg viewBox="0 0 16 13" aria-hidden="true"><path d="M0 1h16v11H0zM2 3v1l6 4 6-4V3L8 7z" fill-rule="evenodd"/></svg>
        info@valtrinautomation.example
      </div>
      <div class="contact-row">
        <svg viewBox="0 0 16 16" aria-hidden="true"><circle cx="8" cy="8" r="7" fill="none" stroke="#047236" stroke-width="1.4"/><path d="M1 8h14M8 1v14" stroke="#047236" stroke-width="1.2"/><ellipse cx="8" cy="8" rx="3.2" ry="7" fill="none" stroke="#047236" stroke-width="1.2"/><path d="M2.5 4.5h11M2.5 11.5h11" stroke="#047236" stroke-width="1"/></svg>
        <span>www.<span class="web-accent">valtrinautomation</span>.example</span>
      </div>
    </div>
  </section>

  <section class="card card-back">
    <div class="brand"><span class="brand-dot"></span>Valtrin Automation</div>
    <div class="tagline-band">Automated Equipment: Design, Build, Control, Test, Support</div>
  </section>

</div>
</body>
</html>
```